Business IT Services Billboard to attract local small businesses

We are Brivolux, a premier Managed Service Provider (MSP) specializing in comprehensive IT services and VOIP phone solutions exclusively for businesses. Our goal is to create a dynamic and visually engaging billboard advertisement that not only highlights our cutting-edge IT solutions but also emphasizes our state-of-the-art VOIP phone services. This billboard should communicate our commitment to providing innovative, reliable, and holistic technology solutions.
Target Market(s)
small business
Industry/Entity Type
Information Technology
Colors
Designer to choose colors to be used in the design.
Look and feel
Each slider illustrates characteristics of the customer's brand and the style your logo design should communicate.

```html
<!DOCTYPE html>
<html lang="en">
<head>
<meta charset="utf-8">
<title>Brivolux – IT and VOIP Billboard</title>
<link rel="stylesheet" href="https://fonts.googleapis.com/css2?family=Montserrat:wght@700;800&family=Catamaran:wght@400&family=Merriweather:ital,wght@1,700&display=swap">
<style>
  :root {
    --page-bg: #e9eef0;
    --board-bg: #f8f8f6;
    --brand-blue: #3f8fc8;
    --stripe-blue: #2c7cc0;
    --accent-grey: #bdbdbd;
    --band-grey: #c4c4c4;
    --text-grey: #7b7b7b;
    --text-dark: #3a3a3a;
    --photo-light: #dfe9f4;
    --photo-mid: #9fb4dc;
    --photo-warm: #e6d2cc;
  }
  html, body {
    margin: 0;
    width: 1200px;
    height: 800px;
    overflow: hidden;
    background: var(--page-bg);
  }
  .billboard {
    position: absolute;
    left: 20px;
    top: 258px;
    width: 1160px;
    height: 284px;
    box-shadow: 0 6px 20px rgba(0,0,0,0.12);
  }
  .headline {
    font-family: "Montserrat", sans-serif;
    font-weight: 800;
    font-size: 26px;
    fill: var(--text-grey);
  }
  .headline .hl { fill: var(--brand-blue); }
  .tagline {
    font-family: "Catamaran", sans-serif;
    font-weight: 400;
    font-size: 20px;
    fill: var(--brand-blue);
  }
  .brand-name {
    font-family: "Montserrat", sans-serif;
    font-weight: 800;
    font-size: 42px;
    fill: var(--brand-blue);
  }
  .cta {
    font-family: "Catamaran", sans-serif;
    font-weight: 400;
    font-size: 17px;
    fill: var(--text-dark);
  }
  .web-address {
    font-family: "Merriweather", serif;
    font-style: italic;
    font-weight: 700;
    font-size: 26px;
    fill: #ffffff;
  }
</style>
</head>
<body>
<svg class="billboard" viewBox="0 0 1160 284" xmlns="http://www.w3.org/2000/svg">
  <defs>
    <linearGradient id="photoTone" x1="0" y1="0" x2="1" y2="1">
      <stop offset="0" stop-color="var(--photo-mid)"/>
      <stop offset="0.55" stop-color="var(--photo-light)"/>
      <stop offset="1" stop-color="var(--photo-warm)"/>
    </linearGradient>
  </defs>

  <rect class="board-surface" width="1160" height="284" fill="var(--board-bg)"/>

  <polygon class="hero-photo" role="img" aria-label="Office desk phone with a hand dialing, overlaid with glowing network and VOIP icons"
           points="0,0 532,0 363,284 0,284" fill="url(#photoTone)"/>

  <polygon class="bottom-band" points="412,249 1160,249 1160,284 388,284" fill="var(--band-grey)"/>
  <polygon class="diagonal-stripe-grey" points="502,83 510,87 393,284 384,284" fill="var(--accent-grey)"/>
  <polygon class="diagonal-stripe-blue" points="523,0 535,0 366,284 354,284" fill="var(--stripe-blue)"/>

  <text class="brand-name" x="641" y="150" text-anchor="middle">Brivolux</text>

  <rect class="divider" x="772" y="0" width="7" height="82" rx="3" fill="var(--accent-grey)"/>

  <text class="headline" text-anchor="middle">
    <tspan x="957" y="55">Elevate <tspan class="hl">Your Business</tspan></tspan>
    <tspan x="957" y="89">with <tspan class="hl">Next-Gen IT</tspan></tspan>
    <tspan x="957" y="123">and <tspan class="hl">VOIP</tspan> Services</tspan>
  </text>

  <text class="tagline" text-anchor="middle">
    <tspan x="957" y="176">Innovative IT and VOIP Solutions</tspan>
    <tspan x="957" y="203">Tailored for Your Business Success.</tspan>
  </text>

  <text class="cta" x="625" y="267" text-anchor="middle">Transform Your Tech Today at:</text>

  <polygon class="url-band" points="809,230 1160,230 1160,284 748,284" fill="var(--brand-blue)"/>
  <text class="web-address" x="990" y="266" text-anchor="middle">www.brivolux.com</text>
</svg>
</body>
</html>
```